Colin Ashbury Racing

I am a racehorse trainer and wish to produce a business card with my details and logo.
The stable colours are Royal blue and black.
The card would need my name and contact details.
Thanks, Colin.

Target Market(s)

Horse owners

Industry/Entity Type

Business

Font styles to use
Serif

Colors
0555a3

Requirements
Must have
• My name. Colour scheme of blue and black.
Nice to have
• Horse or jockey

```html
<!DOCTYPE html>
<html lang="en">
<head>
<meta charset="utf-8">
<title>Colin Ashbury Racing – Business Card</title>
<link rel="stylesheet" href="https://fonts.googleapis.com/css2?family=Source+Sans+3:wght@400;600&display=swap">
<style>
  :root {
    --stage: #e9e9e7;
    --card-white: #f6f6f6;
    --card-black: #1e1e20;
    --royal-blue: #1c55a3;
    --royal-blue-deep: #0f3f86;
    --ink: #2a2a2a;
    --shadow: rgba(0, 0, 0, 0.25);
  }
  * { box-sizing: border-box; margin: 0; padding: 0; }
  html, body {
    width: 1200px;
    height: 1200px;
    overflow: hidden;
    background: var(--stage);
    font-family: "Source Sans 3", "Myriad Pro", sans-serif;
  }
  .stage {
    position: relative;
    width: 1200px;
    height: 1200px;
  }
  .card {
    position: absolute;
    left: 250px;
    width: 700px;
    height: 400px;
    box-shadow: 0 10px 30px var(--shadow);
  }
  .card--front {
    top: 150px;
    background: linear-gradient(115deg, #ffffff 0%, var(--card-white) 55%, #e6e6e6 100%);
  }
  .card--back {
    top: 650px;
    background: linear-gradient(125deg, #2a2a2c 0%, var(--card-black) 50%, #151516 100%);
    display: flex;
    align-items: center;
    justify-content: center;
  }
  .company-name {
    color: var(--royal-blue);
    font-weight: 400;
    letter-spacing: 0.01em;
    text-transform: uppercase;
  }
  .card--front .company-name {
    position: absolute;
    top: 34px;
    right: 40px;
    font-size: 25px;
  }
  .card--back .company-name {
    font-size: 34px;
    color: var(--royal-blue-deep);
  }
  .hero-art {
    position: absolute;
    left: 36px;
    top: 88px;
    width: 330px;
    height: 312px;
    background: linear-gradient(160deg, rgba(28, 85, 163, 0.55) 0%, var(--royal-blue) 60%, rgba(28, 85, 163, 0.8) 100%);
  }
  .identity {
    position: absolute;
    left: 420px;
    top: 186px;
  }
  .identity__name {
    color: var(--royal-blue);
    font-size: 27px;
    font-weight: 400;
    line-height: 1.1;
  }
  .identity__role {
    color: var(--ink);
    font-size: 16px;
    margin-top: 4px;
  }
  .contact-list {
    position: absolute;
    left: 420px;
    top: 282px;
    list-style: none;
  }
  .contact-list__item {
    display: flex;
    align-items: center;
    gap: 10px;
    color: var(--ink);
    font-size: 17px;
    line-height: 26px;
  }
  .contact-list__icon {
    width: 15px;
    height: 15px;
    flex: none;
  }
</style>
</head>
<body>
  <main class="stage">
    <section class="card card--front" aria-label="Business card front">
      <h1 class="company-name">You Companyname Here</h1>
      <div class="hero-art" role="img" aria-label="Royal blue illustration of a rider in a jacket and helmet on a horse jumping a fence"></div>
      <div class="identity">
        <p class="identity__name">Colin Ashbury</p>
        <p class="identity__role">Racehorse Trainer</p>
      </div>
      <ul class="contact-list">
        <li class="contact-list__item">
          <svg class="contact-list__icon" viewBox="0 0 16 16" aria-hidden="true">
            <path fill="var(--royal-blue)" d="M2 5c0-2 2-3 6-3s6 1 6 3v1h-3V5H5v1H2z M4 7h8l2 7H2z"/>
            <circle cx="8" cy="10.5" r="1.8" fill="#fff"/>
          </svg>
          <span>+0 000.000.0000</span>
        </li>
        <li class="contact-list__item">
          <svg class="contact-list__icon" viewBox="0 0 16 16" aria-hidden="true">
            <rect x="1" y="3" width="14" height="10" fill="var(--royal-blue)"/>
            <path d="M1.5 3.5 8 9l6.5-5.5" fill="none" stroke="#fff" stroke-width="1.3"/>
          </svg>
          <span>colinashbury@youcompany.com</span>
        </li>
        <li class="contact-list__item">
          <svg class="contact-list__icon" viewBox="0 0 16 16" aria-hidden="true">
            <circle cx="8" cy="8" r="7" fill="var(--royal-blue)"/>
            <g fill="none" stroke="#fff" stroke-width="1">
              <ellipse cx="8" cy="8" rx="3" ry="7"/>
              <path d="M1 8h14M2.5 4.5h11M2.5 11.5h11"/>
            </g>
          </svg>
          <span>www.yourcompany.com</span>
        </li>
      </ul>
    </section>

    <section class="card card--back" aria-label="Business card back">
      <p class="company-name">You Companyname Here</p>
    </section>
  </main>
</body>
</html>
```